Hypnosis signage

I need a signage 3.50 mt width x 1.60 length.
I'm attaching a signage.
But few changes the Text in the center slightly out of balance.
I'm attaching also photos that can go in one corner.
Please do keep the color orange
Updates

Please I need the signage in Arial Fonts with colors Orange and Black & White for letters or combination
is up to You .

Thank You
Dorian

Colors
f37022

Requirements
Must have
• Clinical Hypnosis
- Weight Loss
- Fear of
Public Speaking
- Anxiety
- Depression
- PTS
- Stop Smoking
- Confidence Building
- Alcohol Moderation

Book now: www.calmtidetrance.net
or call 9462 3089
Should not have
• do You guys see the letters on the signage? "Harbor Sparrows" if You can do the that with Weight Loss ,Stop Smoking, Fear Of Public Speaking , Alcohol Moderation . The letters a bit out of balance .

```html
<!DOCTYPE html>
<html lang="en">
<head>
<meta charset="utf-8">
<title>Clinical Hypnosis Signage</title>
<link rel="stylesheet" href="https://fonts.googleapis.com/css2?family=Arimo:wght@400;700&display=swap">
<style>
  :root {
    --orange: #ec6a22;
    --white: #ffffff;
    --ink: #111111;
    --meadow-light: #f4f1df;
    --meadow-mid: #b9c97a;
    --meadow-deep: #6f8f3a;
    --autumn: #d9a233;
  }
  html, body {
    margin: 0;
    padding: 0;
    overflow: hidden;
    background: var(--white);
  }
  .sign {
    position: relative;
    width: 1200px;
    height: 549px;
    overflow: hidden;
    font-family: "Arimo", Arial, sans-serif;
    color: var(--white);
  }
  .sign__photo {
    position: absolute;
    inset: 0 0 0 420px;
    background:
      radial-gradient(ellipse at 85% 20%, var(--autumn) 0%, rgba(217,162,51,0) 45%),
      radial-gradient(ellipse at 30% 25%, var(--meadow-light) 0%, rgba(244,241,223,0) 55%),
      linear-gradient(180deg, #dfe6c9 0%, var(--meadow-mid) 48%, var(--meadow-deep) 100%);
  }
  .sign__panel {
    position: absolute;
    inset: 0;
    width: 1200px;
    height: 549px;
  }
  .sign__title {
    position: absolute;
    inset: 0;
    width: 1200px;
    height: 140px;
  }
  .sign__title text {
    font-family: "Arimo", Arial, sans-serif;
    font-size: 114px;
    font-weight: 400;
    fill: var(--white);
    stroke: var(--ink);
    stroke-width: 2.5px;
    paint-order: stroke;
  }
  .sign__intro {
    position: absolute;
    left: 36px;
    top: 146px;
    margin: 0;
    font-size: 25px;
    font-weight: 700;
    line-height: 30px;
  }
  .services {
    position: absolute;
    left: 36px;
    top: 208px;
    margin: 0;
    padding: 0;
    list-style: none;
    font-size: 27px;
    font-weight: 700;
    line-height: 35.5px;
  }
  .services li::before {
    content: "• ";
  }
  .sign__note {
    position: absolute;
    left: 36px;
    top: 512px;
    margin: 0;
    font-size: 15px;
    font-weight: 700;
    line-height: 18px;
  }
  .booking {
    position: absolute;
    left: 645px;
    top: 449px;
    width: 537px;
    height: 78px;
    background: var(--orange);
    display: flex;
    flex-direction: column;
    align-items: center;
    justify-content: center;
    font-size: 27px;
    font-weight: 700;
    line-height: 35px;
  }
</style>
</head>
<body>
<div class="sign">
  <div class="sign__photo" role="img" aria-label="Photo of a smiling mature couple embracing in a sunny autumn park"></div>

  <svg class="sign__panel" viewBox="0 0 1200 549" aria-hidden="true">
    <path d="M0 0 H488 C545 80 545 200 497 285 C460 355 468 460 505 549 H0 Z" fill="var(--orange)"/>
    <path d="M488 0 C545 80 545 200 497 285 C460 355 468 460 505 549" fill="none" stroke="var(--white)" stroke-width="6"/>
  </svg>

  <svg class="sign__title" viewBox="0 0 1200 140">
    <text x="24" y="100" textLength="910" lengthAdjust="spacingAndGlyphs">Clinical Hypnosis</text>
  </svg>

  <p class="sign__intro">Clinical Hypnosis can help with</p>

  <ul class="services">
    <li>Weight Loss</li>
    <li>Fear of Public Speaking</li>
    <li>Anxiety</li>
    <li>Depression</li>
    <li>PTS</li>
    <li>Stop Smoking</li>
    <li>Confidence Building</li>
    <li>Alcohol Moderation</li>
  </ul>

  <p class="sign__note">For more information please get in touch</p>

  <div class="booking">
    <span>Book now: Call 9462 3089</span>
    <span>www.calmtidetrance.net</span>
  </div>
</div>
</body>
</html>
```